Frameless shower doors web site

Build a web site for information and display past projects. Contact information, type of work done. Customer Reviews. The design purpose is to generate phone calls and email inquirers. Domain name is Southernshowerdoors.comEmail is Brightpanelworks@mailbarn.com Profile We Love What We Do!Lakeview Bath Panels & Mirror LLC. is committed to excellence in every aspect of our business. We hold a standard of integrity bound by fairness, honesty, and personal responsibility. Our distinction is the quality of service and attention to detail we bring to each project. Above all, we listen to our clients input to provide several design options available from designer glass to hardware. We also service and repair existing shower and tub enclosure. Installation of customer purchased enclosure are available by appointment. and address any concerns.

Target Market(s)

25 to 55 residential customers

Number of Pages Required

4 page

Font styles to use
Sans Serif

Colors

Designer to choose colors to be used in the design.

Requirements
Nice to have
• Looking to drive phone calls for estimating shower projects
Should not have
• Lot of prescriptive words, Clutter

```html
<!DOCTYPE html>
<html lang="en">
<head>
<meta charset="utf-8">
<title>Lakeview Bath Panels & Mirror</title>
<link href="https://fonts.googleapis.com/css2?family=Montserrat:wght@400;600;700&family=Open+Sans:wght@400;600&family=PT+Serif&display=swap" rel="stylesheet">
<style>
:root{
  --canvas:#efefef;
  --navy:#16306f;
  --navy-deep:#0e1f4a;
  --gold:#f5b800;
  --ink:#333;
  --muted:#888;
  --dark:#1a1b22;
  --footer:#17181d;
}
*{margin:0;padding:0;box-sizing:border-box}
html,body{width:1200px;height:1200px;overflow:hidden;background:var(--canvas)}
body{font-family:"Open Sans",sans-serif;color:var(--ink)}
.page{position:absolute;left:384px;top:0;width:433px;height:1200px;background:#fff;overflow:hidden}
.abs{position:absolute}
.serif{font-family:"PT Serif",serif}
.center{text-align:center;transform:translateX(-50%)}
.topbar{left:54px;top:3px;font-size:4px;color:#555}
.topbar b{color:var(--navy);font-size:5px}
.social-dots{left:352px;top:4px;display:flex;gap:4px}
.social-dots i{width:3px;height:3px;border-radius:50%;background:#333;display:block}
.navline{left:0;top:14px;width:433px;height:1px;background:#eee}
.logo{left:54px;top:23px;font:700 9px "Montserrat",sans-serif;color:var(--navy);letter-spacing:.3px}
.nav{left:117px;top:26px;display:flex;gap:10px;font:700 3.4px "Montserrat",sans-serif;color:#333}
.nav .active{color:#2a6fd6}
.search{left:330px;top:23px;width:48px;height:10px;border:1px solid #ccc;font-size:3.5px;color:#aaa;padding:2px 3px}
.hero{left:0;top:42px;width:433px;height:199px;background:linear-gradient(180deg,#5c5f63 0%,#7d8083 45%,#4a4b4e 100%)}
.hero-kicker{left:216px;top:106px;font-size:5px;color:#ddd}
.hero-title{left:216px;top:116px;font:700 18px "Montserrat",sans-serif;color:#fff;white-space:nowrap}
.hero-sub{left:216px;top:136px;font-size:13px;color:#fff;white-space:nowrap}
.btn{background:var(--navy);color:#fff;font:600 4px "Montserrat",sans-serif;display:flex;align-items:center;justify-content:center}
.arrow-circle{width:17px;height:17px;border:1px solid #ccc;border-radius:50%;display:flex;align-items:center;justify-content:center}
.about-frame{left:46px;top:258px;width:132px;height:128px;border:1px solid var(--gold)}
.about-img{left:54px;top:266px;width:132px;height:128px;background:linear-gradient(135deg,#c9ccd0,#9ea3a8 60%,#7c8085)}
.h2{font-size:13px;color:var(--navy)}
.about-p{left:210px;top:306px;width:168px;font-size:3.5px;line-height:1.65;color:#555}
.services{left:0;top:418px;width:433px;height:151px;background:linear-gradient(90deg,#6c7173,#8c8f92 50%,#a5a8ab)}
.svc-label{font-size:5px;color:#fff;text-align:center;width:60px;transform:translateX(-50%);line-height:1.3}
.tile{width:100px;height:56px;display:flex;align-items:center;justify-content:center;text-align:center;color:#fff;font:700 5.5px "Montserrat",sans-serif;line-height:1.35}
.tile span{position:relative}
.tile:after{content:"";position:absolute;inset:3px;border:1px solid rgba(255,255,255,.8)}
.sub{font-size:3.6px;color:#999}
.c-left{left:0;top:910px;width:216px;height:158px;background:linear-gradient(135deg,#22232a,#15161b)}
.c-right{left:216px;top:910px;width:217px;height:158px;background:linear-gradient(135deg,#14275a,#0c1a40)}
.c-item{display:flex;align-items:center;gap:4px;font-size:5px;color:#fff;white-space:nowrap}
.c-item i{width:10px;height:10px;border:1px solid var(--gold);border-radius:50%;display:flex;align-items:center;justify-content:center}
.field{left:243px;width:109px;border:1px solid #5a6ea8;font-size:3.6px;color:#aab;padding:3px}
.footer{left:0;top:1068px;width:433px;height:132px;background:var(--footer)}
.f-h{font:700 4.5px "Montserrat",sans-serif;color:#fff;white-space:nowrap}
.f-h:after{content:"";display:block;width:24px;height:1px;background:var(--gold);margin-top:3px}
.f-list{font-size:3.5px;color:#aaa;line-height:1.95}
.hours{font-size:3.5px;line-height:1.95;color:#ccc;white-space:nowrap}
.hours em{font-style:normal;color:var(--gold);display:inline-block;width:24px}
</style>
</head>
<body>
<main class="page">
  <div class="abs topbar">Got a Plumbing Emergency? <b>Call us : 555-014-2290</b></div>
  <div class="abs social-dots"><i></i><i></i><i></i><i></i></div>
  <div class="abs navline"></div>
  <div class="abs logo">LAKEVIEW</div>
  <nav class="abs nav"><span class="active">HOME</span><span>ABOUT US</span><span>PAST PROJECTS</span><span>SERVICES</span><span>CUSTOMER REVIEWS</span><span>CONTACT US</span></nav>
  <div class="abs search">Search...</div>

  <section class="abs hero" role="img" aria-label="Modern bathroom with floating vanity, wall mirror and green towels"></section>
  <div class="abs hero-kicker center">Clearline</div>
  <div class="abs hero-title center">NEW MODERN COLLECTION</div>
  <div class="abs hero-sub center">For your bathroom</div>
  <div class="abs btn" style="left:194px;top:162px;width:45px;height:15px">COLLECTION</div>
  <div class="abs arrow-circle" style="left:38px;top:133px"><svg width="6" height="6" viewBox="0 0 6 6"><path d="M4 0.5 1.5 3 4 5.5" stroke="#fff" fill="none" stroke-width="0.9"/></svg></div>
  <div class="abs arrow-circle" style="left:379px;top:133px"><svg width="6" height="6" viewBox="0 0 6 6"><path d="M2 0.5 4.5 3 2 5.5" stroke="#fff" fill="none" stroke-width="0.9"/></svg></div>

  <div class="abs about-frame"></div>
  <div class="abs about-img" role="img" aria-label="Bright bathroom with double vanity and large mirror"></div>
  <div class="abs serif h2" style="left:210px;top:277px">About Us</div>
  <div class="abs" style="left:210px;top:295px;font-size:4px;font-style:italic;color:#333">We Love What We Do!</div>
  <p class="abs about-p">Lakeview Bath Panels &amp; Mirror LLC. is committed to excellence in every aspect of our business. We custom build affordable shower enclosures designed to fit your opening perfectly. We are dedicated to making sure that your new shower enclosure fits your needs and has the look you want. Our custom glass shower enclosures will add a distinctive level of class, style and sophistication to any room. We also provide installation and repair service for your current shower enclosure.</p>
  <div class="abs btn" style="left:210px;top:355px;width:49px;height:16px;font-size:4.5px;font-family:'Open Sans',sans-serif">Read More</div>

  <section class="abs services" role="img" aria-label="Bathroom with freestanding tub by a garden window"></section>
  <div class="abs serif" style="left:54px;top:451px;font-size:11px;color:var(--gold)">Services</div>
  <div class="abs" style="left:54px;top:465px;font-size:15px;color:#fff;white-space:nowrap">Areas of Expertise</div>
  <p class="abs" style="left:54px;top:485px;width:132px;font-size:3.4px;line-height:1.6;color:#eee">We design, build and install glass enclosures for every kind of bath, from simple tub panels to full frameless showers and custom mirrors.</p>
  <div class="abs" style="left:54px;top:514px;width:64px;height:19px;background:var(--gold);font-size:5px;color:#222;display:flex;align-items:center;justify-content:center">Read More &nbsp;→</div>
  <svg class="abs" style="left:222px;top:444px" width="22" height="24" viewBox="0 0 22 24" fill="none" stroke="#fff" stroke-width="1"><path d="M5 22V6a4 4 0 0 1 8 0"/><path d="M10 9h8l-2 5h-4z"/></svg>
  <svg class="abs" style="left:285px;top:444px" width="24" height="22" viewBox="0 0 24 22" fill="none" stroke="var(--gold)" stroke-width="1"><path d="M2 10h20l-3 8H5z"/><circle cx="9" cy="5" r="2"/><circle cx="15" cy="4" r="1.5"/></svg>
  <svg class="abs" style="left:350px;top:442px" width="20" height="26" viewBox="0 0 20 26" fill="none" stroke="#fff" stroke-width="1"><ellipse cx="9" cy="13" rx="7" ry="11"/><path d="M7 16l4-6"/></svg>
  <div class="abs svc-label" style="left:233px;top:475px">Frameless Shower Enclosures</div>
  <div class="abs svc-label" style="left:296px;top:475px;color:var(--gold)">Tub Enclosures</div>
  <div class="abs svc-label" style="left:359px;top:475px">Custom Mirrors</div>
  <svg class="abs" style="left:224px;top:502px" width="18" height="28" viewBox="0 0 18 28" fill="none" stroke="#fff" stroke-width="1"><path d="M9 1l7 4v8l-7 4-7-4V5z"/><path d="M7 17h4v10H7z"/></svg>
  <svg class="abs" style="left:283px;top:502px" width="26" height="26" viewBox="0 0 26 26" fill="none" stroke="#fff" stroke-width="1"><circle cx="13" cy="12" r="11"/><circle cx="13" cy="12" r="7"/><path d="M13 23v3"/></svg>
  <div class="abs svc-label" style="left:233px;top:538px">Installation &amp; Repairs</div>
  <div class="abs svc-label" style="left:296px;top:538px">Glass &amp; Mirror</div>

  <div class="abs serif center" style="left:216px;top:589px;font-size:12px;color:var(--navy);white-space:nowrap">Our Gallery</div>
  <div class="abs sub center" style="left:216px;top:607px;white-space:nowrap">Lakeview Bath Panels &amp; Mirror LLC.</div>
  <div class="abs tile" style="left:54px;top:633px;background:linear-gradient(135deg,#59616b,#8a9199)" role="img" aria-label="Bright bath with glass shower"><span>LAKEVIEW BATH<br>PANELS &amp; MIRROR</span></div>
  <div class="abs tile" style="left:167px;top:633px;background:linear-gradient(135deg,#1d3566,#3a5382)" role="img" aria-label="Remodeled bathroom"><span>BATHROOM REMODEL</span></div>
  <div class="abs tile" style="left:279px;top:633px;background:linear-gradient(135deg,#5b4a3c,#1b2c5c)" role="img" aria-label="Frameless shower in tiled room"><span>FRAME-LESS SHOWER</span></div>
  <div class="abs tile" style="left:54px;top:701px;background:linear-gradient(135deg,#4a3a30,#7a6455)" role="img" aria-label="Glass shower with stone tile"><span>LAKEVIEW BATH<br>PANELS &amp; MIRROR</span></div>
  <div class="abs tile" style="left:167px;top:701px;background:linear-gradient(135deg,#a08c75,#cdbba2)" role="img" aria-label="Tiled walk-in shower"><span>BATHROOM REMODEL</span></div>
  <div class="abs tile" style="left:279px;top:701px;background:linear-gradient(135deg,#aeb4ba,#d8dcdf)" role="img" aria-label="Clear glass shower enclosure"><span>FRAME-LESS SHOWER</span></div>

  <div class="abs serif center" style="left:216px;top:778px;font-size:12px;color:var(--navy);white-space:nowrap">Customer Review</div>
  <div class="abs sub center" style="left:216px;top:795px;white-space:nowrap">Lakeview Bath Panels &amp; Mirror LLC.</div>
  <svg class="abs" style="left:201px;top:813px" width="30" height="34" viewBox="0 0 30 34" role="img" aria-label="Reviewer portrait"><path d="M15 1l13 8v16l-13 8-13-8V9z" fill="#3b4a66" stroke="#9aa8c4" stroke-width="1"/></svg>
  <div class="abs" style="left:81px;top:843px;width:13px;height:14px;background:#eee;display:flex;align-items:center;justify-content:center;font-size:6px;color:#555">‹</div>
  <div class="abs" style="left:339px;top:843px;width:13px;height:14px;background:#eee;display:flex;align-items:center;justify-content:center;font-size:6px;color:#555">›</div>
  <div class="abs center" style="left:216px;top:853px;width:240px;font-size:3.6px;line-height:1.7;color:#444;text-align:center">Owen explains what needs to be done and he gets right to work. Excellent job and and a gentleman.<br>Owen had what he needed to fix shower door with him. Dana R</div>
  <div class="abs center" style="left:216px;top:866px;font-size:5px;color:var(--gold);letter-spacing:1px">★★★★</div>
  <div class="abs center" style="left:216px;top:875px;font-size:4px;font-style:italic;color:var(--navy);white-space:nowrap">Dana R. in Elm Grove, TX</div>
  <div class="abs center" style="left:216px;top:882px;font-size:3.6px;color:#777;white-space:nowrap">Repair Existing Shower Door or Enclosure</div>

  <div class="abs c-left" role="img" aria-label="Dimmed photo of a person on a phone"></div>
  <div class="abs c-right"></div>
  <div class="abs serif center" style="left:130px;top:948px;font-size:10px;color:var(--gold);white-space:nowrap">Contact Information</div>
  <div class="abs sub center" style="left:130px;top:965px;white-space:nowrap">Lakeview Bath Panels &amp; Mirror LLC.</div>
  <div class="abs c-item" style="left:78px;top:984px"><i><svg width="5" height="5" viewBox="0 0 10 10"><path d="M2 1l2 2-1 1.5 2.5 2.5L7 6l2 2-1.5 1.5C4 9 1 6 .5 2.5z" fill="#fff"/></svg></i>555-014-2290</div>
  <div class="abs c-item" style="left:78px;top:1000px"><i><svg width="5" height="4" viewBox="0 0 10 8"><rect x="0.5" y="0.5" width="9" height="7" fill="none" stroke="#fff"/><path d="M.5 .5 5 4.5 9.5.5" fill="none" stroke="#fff"/></svg></i>Brightpanelworks@mailbarn.com</div>
  <div class="abs c-item" style="left:78px;top:1016px"><i><svg width="4" height="5" viewBox="0 0 8 10"><path d="M4 10C1 6 0 4.5 0 4a4 4 0 0 1 8 0c0 .5-1 2-4 6z" fill="#fff"/></svg></i>218 Harbor Mill Rd, Lakeview, TX 75099</div>
  <div class="abs serif center" style="left:297px;top:922px;font-size:10px;color:var(--gold);white-space:nowrap">Contact Form</div>
  <div class="abs center" style="left:297px;top:939px;font-size:4.4px;color:#ddd;white-space:nowrap">Lakeview Bath Panels &amp; Mirror LLC.</div>
  <div class="abs field" style="top:959px;height:13px">Name</div>
  <div class="abs field" style="top:977px;height:13px">Email</div>
  <div class="abs field" style="top:995px;height:13px">Phone</div>
  <div class="abs field" style="top:1014px;height:24px">Message</div>
  <div class="abs" style="left:243px;top:1043px;width:31px;height:11px;background:#fff;color:var(--navy);font-size:3.6px;display:flex;align-items:center;justify-content:center">SUBMIT</div>

  <footer class="abs footer"></footer>
  <div class="abs f-h" style="left:54px;top:1088px">About</div>
  <div class="abs logo" style="top:1109px;color:#fff">LAKEVIEW</div>
  <p class="abs f-list" style="left:54px;top:1126px;width:70px;line-height:1.7">Lakeview Bath Panels &amp; Mirror LLC. is committed to excellence in every</p>
  <div class="abs social-dots" style="left:54px;top:1153px;gap:4px"><i style="width:8px;height:8px;border:1px solid #ccc;background:none"></i><i style="width:8px;height:8px;border:1px solid #ccc;background:none"></i><i style="width:8px;height:8px;border:1px solid #ccc;background:none"></i><i style="width:8px;height:8px;border:1px solid #ccc;background:none"></i></div>
  <div class="abs f-h" style="left:150px;top:1088px">Homeowner Services</div>
  <div class="abs f-list" style="left:150px;top:1100px">Pro Match<br>Pro Reviews<br>Emergency Repairs<br>Write a Review<br>Find Local Pros</div>
  <div class="abs f-h" style="left:232px;top:1088px">Business Hours</div>
  <div class="abs hours" style="left:232px;top:1100px"><em>Monday :</em>8:00 AM to 5:00 PM<br><em>Tuesday :</em>8:00 AM to 5:00 PM<br><em>Wednesday :</em>8:00 AM to 5:00 PM<br><em>Thursday :</em>8:00 AM to 5:00 PM<br><em>Friday :</em>8:00 AM to 5:00 PM<br><em>Saturday :</em>9:00 AM to 3:00 PM</div>
  <div class="abs f-h" style="left:322px;top:1088px">Homeowner Resources</div>
  <div class="abs f-list" style="left:322px;top:1100px">My Account<br>Project Cost Notes<br>Resource Center<br>Refer a Pro<br>Pros Near Me<br>Home Ideas Blog</div>
  <div class="abs" style="left:150px;top:1154px;font:600 5px 'Montserrat',sans-serif;color:#fff;white-space:nowrap">Newsletter sign up</div>
  <div class="abs" style="left:202px;top:1153px;width:72px;height:9px;border:1px solid #444;font-size:3px;color:#888;padding:2px 3px">Enter your email...</div>
  <div class="abs" style="left:275px;top:1153px;width:29px;height:9px;background:var(--gold);font:600 3.6px 'Montserrat',sans-serif;color:#222;display:flex;align-items:center;justify-content:center">Subscribe</div>
  <div class="abs center" style="left:216px;top:1189px;font-size:3.4px;color:#888;white-space:nowrap">@ Copyright Brightpanelworks.com 2019</div>
</main>
</body>
</html>
```